This project is to address Personal Life issues/ Health & Wellness using a certified Professional Coaching Approach.

Major coaching areas include: Weight loss, Overwhelm/ Time Management, Increased Energy, Leadership, Improved Relationships, Finding Your Life Purpose & passion, Self Esteem & Confidence,

The combination of a board certified Internal Medicine physician and
professional coach is a powerful and unique approach to help people achieve
better health and well being.

Target Market(s)

Existing or potentially new patients/clients interested in any of the listed categories of coaching.

Industry/Entity Type

Life Coaching

Font styles to use
Sans Serif

Colors
00a990
0292cd
0255a3
33b8a4
a64599
6b449b
876aae
3176b5
33a6d7

Requirements
Must have
• Design specifics: Use of deep blues/greens using nature imagery is
• preferred- see our website for at Brightvalecaredoc.com
• Each category of coaching must be listed out with a paragraph of description below each- I will provide the description in an attachment that is pending.
• Title of Brochure: "Clearbrook Health Personal Life & Wellness Coaching."
• "Coaching That Works!"
Nice to have
• A definition of coaching on the front of brochure:
• " A compassionate catalyzing relationship - The art of facilitating the performance, learning and development of another so they may achieve what the want faster.”
• Also on the front please place: "Stuck? Ask about a free coaching consult with Dr. Tavren to learn more!"
Should not have
• Should not have anything in the brochure that mentions medical services from the website outside of weight loss. The purpose of the brochure is to promote the coaching services.

```html
<!DOCTYPE html>
<html lang="en">
<head>
<meta charset="utf-8">
<title>Clearbrook Health Personal Life &amp; Wellness Coaching – Trifold Brochure</title>
<link rel="stylesheet" href="https://fonts.googleapis.com/css2?family=Cinzel:wght@500;700&family=Dancing+Script:wght@600;700&family=Lora:ital,wght@0,600;1,500&family=Open+Sans:ital,wght@0,400;0,600;0,700;1,400&display=swap">
<style>
  :root{
    --backdrop:#e4e5e6;
    --paper:#f4f5f6;
    --navy:#0b2c78;
    --blue:#0255a3;
    --blue-mid:#3176b5;
    --sky:#33a6d7;
    --teal:#00a990;
    --teal-light:#33b8a4;
    --green-script:#1f9a5a;
    --ink:#4a4f57;
    --white:#ffffff;
  }
  *{box-sizing:border-box;margin:0;padding:0}
  html,body{width:1200px;height:2400px;overflow:hidden}
  body{background:var(--backdrop);font-family:"Open Sans",Arial,sans-serif;color:var(--ink);position:relative}

  .spread{position:absolute;left:60px;width:1080px;height:835px;background:var(--paper);overflow:hidden;box-shadow:0 18px 40px rgba(0,0,0,.18)}
  .spread--outside{top:250px}
  .spread--inside{top:1315px}
  .spread__art{position:absolute;inset:0;width:1080px;height:835px}
  .fold{position:absolute;top:0;width:1px;height:835px;background:rgba(0,0,0,.06)}
  .fold--one{left:360px}.fold--two{left:720px}

  .block{position:absolute}

  /* outside: about panel */
  .doctor-tag{left:36px;top:34px;padding:6px 22px;background:var(--blue);color:var(--white);font-family:"Lora",Georgia,serif;font-style:italic;font-size:15px;border-radius:16px}
  .about-heading{left:30px;top:84px;width:300px;text-align:center;font-family:"Dancing Script",cursive;color:var(--green-script);font-size:27px;line-height:1.15}
  .about-lead{left:34px;top:170px;width:292px;text-align:center;font-style:italic;color:var(--teal);font-size:13.5px;line-height:1.45}
  .about-body{left:34px;top:278px;width:292px;text-align:center;font-size:11.5px;line-height:1.5;color:var(--ink)}

  /* outside: contact panel */
  .contact-heading{left:360px;top:450px;width:360px;text-align:center;font-family:"Dancing Script",cursive;color:var(--teal-light);font-size:36px}
  .contact-phone{left:410px;top:510px;width:260px;height:40px;border-radius:20px;background:var(--teal);color:var(--white);display:flex;align-items:center;gap:14px;padding-left:8px;font-size:22px;font-weight:600;letter-spacing:.5px}
  .contact-phone__icon{width:28px;height:28px;border-radius:50%;background:var(--white);display:flex;align-items:center;justify-content:center}
  .contact-lines{left:360px;top:570px;width:360px;text-align:center;color:var(--white);font-size:13px;line-height:1.7}
  .contact-web{left:360px;top:735px;width:360px;text-align:center;color:var(--white);font-weight:700;font-size:17px;letter-spacing:.3px}

  /* outside: cover panel */
  .brand{left:760px;top:500px;width:280px;display:flex;flex-direction:column;align-items:center;gap:6px}
  .brand__mark{width:54px;height:54px;border-radius:50%;background:var(--blue)}
  .brand__name{font-family:"Cinzel",Georgia,serif;font-weight:700;color:var(--navy);font-size:15px;letter-spacing:1px}
  .cover-title{left:720px;top:592px;width:360px;text-align:center;font-family:"Cinzel",Georgia,serif;font-weight:500;color:var(--blue-mid);font-size:14.5px;line-height:1.35;letter-spacing:.3px;white-space:nowrap}
  .cover-tagline{left:720px;top:648px;width:360px;text-align:center;font-family:"Dancing Script",cursive;color:var(--green-script);font-size:33px;line-height:1.2}
  .cover-web{left:762px;top:722px;width:276px;height:38px;border-radius:19px;background:var(--blue);color:var(--white);font-weight:700;font-size:16px;display:flex;align-items:center;justify-content:center}

  /* inside panels */
  .services-banner{left:0;top:44px;width:250px;padding:7px 0 7px 30px;background:var(--teal-light);color:var(--white);font-family:"Cinzel",Georgia,serif;font-size:17px;letter-spacing:1px;border-radius:0 18px 18px 0}
  .service{position:absolute}
  .service__title{font-family:"Lora",Georgia,serif;font-weight:600;font-size:20px;line-height:1.25;margin-bottom:6px}
  .service__text{font-size:12px;line-height:1.55}
  .service__text + .service__text{margin-top:10px}
  .service--dark .service__title{color:var(--teal-light)}
  .service--dark .service__text{color:#dfe7f5}
  .service--light .service__title{color:var(--blue)}
  .service--light .service__text{color:var(--ink)}
</style>
</head>
<body>

<section class="spread spread--outside" aria-label="Brochure outside">
  <svg class="spread__art" viewBox="0 0 1080 835">
    <defs>
      <linearGradient id="sky-meadow" x1="0" y1="0" x2="0" y2="1">
        <stop offset="0" stop-color="#cfe0ef"/><stop offset=".45" stop-color="#8fb0c4"/><stop offset=".6" stop-color="#4f7d5a"/><stop offset="1" stop-color="#8fb24a"/>
      </linearGradient>
      <linearGradient id="studio" x1="0" y1="0" x2="1" y2="1">
        <stop offset="0" stop-color="#c9dbe6"/><stop offset="1" stop-color="#6d8fb0"/>
      </linearGradient>
      <radialGradient id="lotus" cx=".5" cy=".5" r=".6">
        <stop offset="0" stop-color="#f5f7f0"/><stop offset=".5" stop-color="#b8d49a"/><stop offset="1" stop-color="#3f7a3c"/>
      </radialGradient>
      <clipPath id="clip-about"><rect x="0" y="0" width="360" height="835"/></clipPath>
      <clipPath id="clip-cover"><rect x="380" y="0" width="700" height="835"/></clipPath>
    </defs>

    <rect class="panel-contact" x="360" y="0" width="360" height="835" fill="var(--navy)"/>

    <g clip-path="url(#clip-about)">
      <ellipse cx="140" cy="615" rx="205" ry="170" fill="var(--navy)"/>
      <ellipse cx="132" cy="615" rx="192" ry="160" fill="var(--teal-light)"/>
      <g role="img" aria-label="Photo of a group yoga class stretching in a bright studio">
        <ellipse cx="128" cy="615" rx="186" ry="154" fill="url(#studio)"/>
      </g>
    </g>

    <circle cx="540" cy="330" r="62" fill="var(--teal)"/>
    <g role="img" aria-label="Photo of a white water lily on green leaves">
      <circle cx="540" cy="330" r="54" fill="url(#lotus)"/>
    </g>

    <g clip-path="url(#clip-cover)">
      <circle cx="905" cy="245" r="262" fill="var(--paper)"/>
      <circle cx="905" cy="245" r="250" fill="var(--teal)"/>
      <g role="img" aria-label="Photo of a woman with arms raised in a green meadow before mountains">
        <circle cx="905" cy="245" r="238" fill="url(#sky-meadow)"/>
      </g>
    </g>
  </svg>
  <span class="fold fold--one"></span><span class="fold fold--two"></span>

  <p class="block doctor-tag">Dr. Elan Tavren MD</p>
  <h2 class="block about-heading">Clearbrook Health<br>Medicine That Works!</h2>
  <p class="block about-lead">The combination of a board certified Internal Medicine physician and professional coach is a powerful and unique approach to help people achieve better health and well being.</p>
  <p class="block about-body">Dr. Tavren has practiced internal medicine for many years and now pairs that care with certified coaching to guide clients toward lasting change.</p>

  <h2 class="block contact-heading">Contact Us</h2>
  <p class="block contact-phone">
    <span class="contact-phone__icon">
      <svg width="16" height="16" viewBox="0 0 24 24" aria-hidden="true"><path fill="var(--teal)" d="M6.6 10.8a15.1 15.1 0 0 0 6.6 6.6l2.2-2.2a1 1 0 0 1 1-.25 11.4 11.4 0 0 0 3.6.57 1 1 0 0 1 1 1V20a1 1 0 0 1-1 1A17 17 0 0 1 3 4a1 1 0 0 1 1-1h3.5a1 1 0 0 1 1 1c0 1.25.2 2.45.57 3.6a1 1 0 0 1-.25 1z"/></svg>
    </span>
    555.014.2270
  </p>
  <p class="block contact-lines">office.tavren@brightvalemail.com<br>2270 Millbrook Ave. Riverton, Tx 70000</p>
  <p class="block contact-web">www.brightvalecaredoc.com</p>

  <div class="block brand">
    <span class="brand__mark"></span>
    <span class="brand__name">Clearbrook Health MD</span>
  </div>
  <h1 class="block cover-title">Clearbrook Health Personal Life &amp;<br>Wellness Coaching</h1>
  <p class="block cover-tagline">Coaching That Works!</p>
  <p class="block cover-web">www.brightvalecaredoc.com</p>
</section>

<section class="spread spread--inside" aria-label="Brochure inside">
  <svg class="spread__art" viewBox="0 0 1080 835">
    <defs>
      <linearGradient id="sunset-field" x1="0" y1="0" x2="1" y2="1">
        <stop offset="0" stop-color="#f4d27a"/><stop offset=".5" stop-color="#b6a24a"/><stop offset="1" stop-color="#4f7a3a"/>
      </linearGradient>
      <radialGradient id="food" cx=".5" cy=".5" r=".6">
        <stop offset="0" stop-color="#f2e4c4"/><stop offset=".6" stop-color="#d98a4a"/><stop offset="1" stop-color="#7a9a4a"/>
      </radialGradient>
      <linearGradient id="city-run" x1="0" y1="0" x2="1" y2="1">
        <stop offset="0" stop-color="#f3dcb6"/><stop offset=".5" stop-color="#d9b48a"/><stop offset="1" stop-color="#6f8fae"/>
      </linearGradient>
      <clipPath id="clip-runner"><rect x="720" y="0" width="360" height="835"/></clipPath>
    </defs>

    <path d="M0 0 H330 C 430 180 300 380 400 560 L400 835 H0 Z" fill="var(--navy)"/>
    <path d="M330 0 C 430 180 300 380 400 560" fill="none" stroke="var(--teal-light)" stroke-width="6"/>

    <path d="M0 640 C 140 575 300 660 470 600 L470 835 H0 Z" fill="var(--teal-light)"/>
    <g role="img" aria-label="Photo of a woman with open arms in a sunlit field">
      <path d="M0 652 C 140 588 300 672 470 612 L470 835 H0 Z" fill="url(#sunset-field)"/>
    </g>

    <circle cx="470" cy="680" r="62" fill="var(--teal)"/>
    <g role="img" aria-label="Photo of a plate of fresh fruit and healthy food">
      <circle cx="470" cy="680" r="54" fill="url(#food)"/>
    </g>

    <g clip-path="url(#clip-runner)">
      <circle cx="930" cy="705" r="232" fill="var(--teal-light)"/>
      <g role="img" aria-label="Photo of a young woman resting after a run in the city">
        <circle cx="930" cy="705" r="222" fill="url(#city-run)"/>
      </g>
    </g>
  </svg>
  <span class="fold fold--one"></span><span class="fold fold--two"></span>

  <h2 class="block services-banner">Coaching Services</h2>

  <article class="service service--dark" style="left:30px;top:100px;width:280px">
    <h3 class="service__title">Weight Loss</h3>
    <p class="service__text">Two thirds of adults carry extra weight. Coaching builds steady habits around food, movement and sleep so results last.</p>
  </article>
  <article class="service service--dark" style="left:30px;top:270px;width:285px">
    <h3 class="service__title">Overwhelm &amp; Time Management</h3>
    <p class="service__text">Too much on your plate? We sort priorities, set limits and free up time for what matters most to you.</p>
  </article>

  <article class="service service--light" style="left:420px;top:40px;width:270px">
    <h3 class="service__title">Increased Energy</h3>
    <p class="service__text">Low energy often signals stress or poor rest. Together we find the habits that restore your drive and focus.</p>
  </article>
  <article class="service service--light" style="left:400px;top:195px;width:290px">
    <h3 class="service__title">Leadership</h3>
    <p class="service__text">Strong leaders lead themselves first. Coaching sharpens vision, clear communication and the confidence to guide others.</p>
  </article>
  <article class="service service--light" style="left:430px;top:345px;width:260px">
    <h3 class="service__title">Improved Relationships</h3>
    <p class="service__text">Healthy connections shape health and happiness. Learn to listen, speak openly and build trust at home and at work.</p>
  </article>

  <article class="service service--light" style="left:750px;top:40px;width:300px">
    <h3 class="service__title">Finding Your Life Purpose</h3>
    <p class="service__text">Feeling adrift? We explore your values, strengths and passions to uncover a purpose that gives each day meaning.</p>
    <p class="service__text">Fulfillment grows when your goals match who you truly are.</p>
  </article>
  <article class="service service--light" style="left:750px;top:265px;width:300px">
    <h3 class="service__title">Confidence/Self Esteem</h3>
    <p class="service__text">Self doubt holds many people back. Coaching helps you quiet the inner critic and act with calm assurance.</p>
    <p class="service__text">Building Confidence is a process.</p>
  </article>
</section>

</body>
</html>
```